Business card for Verano Living

Hi again, I need a business card for my Verano Living business you have been working on with the following information:

Clara Hollis
Director
m. 0412 736 258
e. clara@veranoliving-example.com.au
w. www.veranoliving-example.com.au

Maybe you could use the original design (using both the green & white) and where the white box is you could include the above details (name / mobile / etc) - Perhaps the 'i' in Clara could be the bow tie again?

Then the back could be green with black writing stating:

Services Offered:

* Personal Assistant Concierge
* Decluttering Concierge
* Home Management Concierge
* FIFO Concierge
* Events Concierge
* Leisure & Travel Concierge
* Seasonal Concierge
* Professional Concierge

Many thanks
Updates

Hi Everyone I'm really sorry but I am working with just one designer on this brief, thank you for your work and apologies for my error.

Industry/Entity Type

Business

```html
<!DOCTYPE html>
<html lang="en">
<head>
<meta charset="utf-8">
<title>Verano Living – Business Card</title>
<link rel="stylesheet" href="https://fonts.googleapis.com/css2?family=Exo+2:wght@300;400&family=Pinyon+Script&display=swap">
<style>
  :root {
    --canvas-bg: #ececea;
    --card-green: #64a533;
    --name-green: #5c9d2c;
    --card-white: #ffffff;
    --ink: #1d1d1b;
    --light-text: #f4f8ee;
    --card-shadow: rgba(0, 0, 0, 0.18);
  }
  * { margin: 0; padding: 0; box-sizing: border-box; }
  html, body {
    width: 1200px;
    height: 873px;
    overflow: hidden;
    background: var(--canvas-bg);
  }
  .canvas {
    width: 1200px;
    height: 873px;
    display: flex;
    align-items: center;
    justify-content: center;
    gap: 40px;
  }
  .card {
    position: relative;
    width: 540px;
    height: 309px;
    background: var(--card-green);
    box-shadow: 0 6px 18px var(--card-shadow);
    font-family: "Exo 2", sans-serif;
    overflow: hidden;
  }

  /* Wordmark: plain name with a single square marker */
  .wordmark {
    position: absolute;
    left: 28px;
    top: 24px;
    display: flex;
    align-items: center;
    gap: 12px;
  }
  .wordmark-square {
    width: 16px;
    height: 16px;
    background: var(--light-text);
  }
  .wordmark-name {
    font-family: "Exo 2", sans-serif;
    font-weight: 400;
    font-size: 30px;
    line-height: 1;
    color: var(--light-text);
  }
  .tagline {
    position: absolute;
    left: 56px;
    top: 62px;
    font-family: "Exo 2", sans-serif;
    font-weight: 400;
    font-size: 12px;
    letter-spacing: 2.5px;
    text-transform: uppercase;
    color: var(--light-text);
  }

  /* Front */
  .front .contact-panel {
    position: absolute;
    left: 0;
    right: 0;
    top: 92px;
    height: 150px;
    background: var(--card-white);
  }
  .front .person {
    position: absolute;
    right: 28px;
    top: 16px;
    text-align: right;
  }
  .front .person-name {
    font-weight: 400;
    font-size: 34px;
    line-height: 1.05;
    color: var(--name-green);
  }
  .front .person-role {
    font-family: "Pinyon Script", cursive;
    font-size: 26px;
    line-height: 1.15;
    color: var(--ink);
  }
  .front .person-phone {
    font-weight: 400;
    font-size: 24px;
    line-height: 1.2;
    color: var(--ink);
  }
  .front .web-details {
    position: absolute;
    right: 28px;
    bottom: 12px;
    text-align: right;
    font-size: 16px;
    line-height: 1.3;
    color: var(--ink);
  }

  /* Back */
  .back .services {
    position: absolute;
    left: 28px;
    top: 118px;
    list-style: none;
    font-weight: 300;
    font-size: 16px;
    line-height: 1.55;
    color: var(--light-text);
  }
  .back .services .divider { margin: 0 6px; }
</style>
</head>
<body>
<main class="canvas">

  <section class="card front" aria-label="Business card front">
    <div class="wordmark">
      <span class="wordmark-square" aria-hidden="true"></span>
      <span class="wordmark-name">Verano Living</span>
    </div>
    <div class="contact-panel">
      <div class="person">
        <div class="person-name">Clara Hollis</div>
        <div class="person-role">Director</div>
        <div class="person-phone">0412 736 258</div>
      </div>
    </div>
    <div class="web-details">
      <div class="email">clara@veranoliving-example.com.au</div>
      <div class="website">www.veranoliving-example.com.au</div>
    </div>
  </section>

  <section class="card back" aria-label="Business card back">
    <div class="wordmark">
      <span class="wordmark-square" aria-hidden="true"></span>
      <span class="wordmark-name">Verano Living</span>
    </div>
    <div class="tagline">Your Personal Concierge</div>
    <ul class="services">
      <li>Personal Assistant Concierge<span class="divider">|</span>Decluttering Concierge</li>
      <li>Home Management Concierge<span class="divider">|</span>FIFO Concierge</li>
      <li>Events Concierge<span class="divider">|</span>Leisure &amp; Travel Concierge</li>
      <li>Seasonal Concierge<span class="divider">|</span>Professional Concierge</li>
    </ul>
  </section>

</main>
</body>
</html>
```